Wordpress Design Project

Specifications - we are after the design for a Wordpress Template. The template files need to be uploaded through the Wordpress templates upload button.
Facebook button required please
The template must also work and integrate with Wordpress.
We are after a sharp, professional look, that will be appealing to business clients as well as other customers requiring this service
refer to www.nova-rankers.com.au
www.lanai-vornby.com.au
Please create a logo.

Client Industry - Corporate and Mobile Massage
Header Colour - Charcoal/black with Purple/Crimson. All lettering on the header should appear in white or purple
Page colour - white
Other - rhs sidebar; easy to insert images on pages
Toolbar - horizontal below header - refer to two sites above for ideas.
This will be a 5 - 7 page site only.

Target Market(s)

Corporate and business massage - large businesses/government departments

Requirements
Must have
• The template files need to be uploaded through the Wordpress templates upload button.
Nice to have
• A logo

```html
<!DOCTYPE html>
<html lang="en">
<head>
<meta charset="utf-8">
<title>Calm Harbour — On Location &amp; Workplace Massage</title>
<link href="https://fonts.googleapis.com/css2?family=Cinzel:wght@400;600&family=Tinos:wght@400;700&display=swap" rel="stylesheet">
<style>
  :root {
    --page: #ffffff;
    --header-dark: #240a29;
    --header-mid: #3a1242;
    --nav-top: #4c1b58;
    --nav-bottom: #2a0c31;
    --nav-divider: #1c0620;
    --lilac: #f3dcf5;
    --orange: #f7a20f;
    --orange-deep: #ef9a0c;
    --crimson: #d3165a;
    --plum: #5b1a63;
    --magenta: #88217b;
    --pink-head: #c51a78;
    --link-purple: #6b2a8a;
    --ink: #1c1a1c;
    --night: #0d0a08;
    --footer: #e6e5ec;
    --rule: #c9c9c9;
  }
  * { box-sizing: border-box; margin: 0; padding: 0; }
  html, body { width: 1200px; height: 1189px; overflow: hidden; background: var(--page); }
  body { position: relative; font-family: "Cinzel", serif; color: var(--ink); }

  .page-frame { position: absolute; top: 0; left: 68px; width: 1064px; height: 1189px;
    border-left: 1px solid var(--rule); border-right: 1px solid var(--rule); }

  /* Header */
  .site-header { position: absolute; left: 79px; top: 0; width: 1042px; height: 194px;
    background: radial-gradient(ellipse at 55% 20%, var(--header-mid), var(--header-dark) 70%); }
  .brand { position: absolute; left: 28px; top: 92px; color: var(--lilac); }
  .brand-name { font-size: 40px; font-weight: 400; letter-spacing: 1px; line-height: 1; }
  .brand-tagline { font-size: 17px; margin-top: 8px; margin-left: 86px; text-transform: lowercase; }

  .social { position: absolute; top: 23px; display: flex; height: 27px; border-radius: 4px; overflow: hidden;
    font-family: "Tinos", serif; font-size: 11px; font-weight: 700; color: #fff; }
  .social .icon { width: 28px; }
  .social .count { width: 41px; display: flex; align-items: center; justify-content: center; }
  .social .join { width: 36px; display: flex; align-items: center; justify-content: center; }
  .social.one { left: 793px; background: #55b8dc; }
  .social.one .icon { background: #2c9bd0; }
  .social.one .join { background: #3aa5d6; }
  .social.two { left: 904px; background: #5571b2; }
  .social.two .icon { background: #3b5998; }
  .social.two .join { background: #4562a5; }

  .contact { position: absolute; right: 27px; top: 70px; text-align: right; }
  .phone { color: var(--orange); font-size: 15px; font-variant: small-caps; }
  .phone strong { font-size: 20px; font-weight: 400; }
  .message-link { display: block; color: var(--crimson); font-size: 13px; font-variant: small-caps; margin-top: 8px; letter-spacing: 0.5px; }
  .util-links { position: absolute; right: 27px; top: 148px; display: flex; gap: 72px;
    color: #fff; font-size: 14px; letter-spacing: 0.8px; }

  /* Navigation */
  .main-nav { position: absolute; left: 79px; top: 194px; width: 1042px; height: 66px;
    background: linear-gradient(var(--nav-top), var(--nav-bottom)); display: flex; }
  .main-nav a { color: #fff; text-decoration: none; font-size: 16px; letter-spacing: 0.6px;
    display: flex; align-items: center; padding: 0 16px; border-right: 2px solid var(--nav-divider); }
  .main-nav a:first-child { padding-left: 29px; }
  .main-nav a:last-child { border-right: 0; }

  /* Hero */
  .hero { position: absolute; left: 79px; top: 264px; width: 1042px; height: 446px; }
  .hero-photo { position: absolute; left: 0; top: 0; width: 468px; height: 446px;
    background: radial-gradient(ellipse at 60% 55%, #f2a23a, #d36f10 55%, #5d3b10); }
  .hero-panel { position: absolute; left: 468px; top: 0; width: 333px; height: 446px; background: var(--orange);
    padding: 90px 14px 0 22px; color: #fff; }
  .hero-panel h2 { font-weight: 400; font-size: 19px; line-height: 1.15; letter-spacing: 0.5px; }
  .hero-panel p { font-size: 13px; line-height: 1.3; margin-top: 18px; letter-spacing: 0.4px; }
  .hero-panel h3 { font-weight: 400; font-size: 19px; line-height: 1.15; color: var(--crimson); margin-top: 20px; letter-spacing: 0.5px; }
  .hero-panel .where { font-size: 13px; margin-top: 42px; letter-spacing: 0.6px; }
  .hero-panel .options { display: flex; gap: 62px; margin-top: 22px; font-size: 13px; letter-spacing: 0.6px; }

  .hero-tabs { position: absolute; left: 801px; top: 0; height: 446px; display: flex; }
  .tab { height: 446px; position: relative; color: #fff; font-size: 17px; letter-spacing: 0.6px; }
  .tab span { position: absolute; bottom: 26px; left: 50%; transform-origin: left center;
    transform: translateX(-50%) rotate(-90deg) translateX(0); white-space: nowrap; }
  .tab span { transform: none; writing-mode: vertical-rl; rotate: 180deg; left: 0; right: 0; margin: auto; width: 20px; }
  .tab.massage { width: 58px; background: var(--orange-deep); box-shadow: inset 2px 0 0 #d98b06; }
  .tab.facial { width: 60px; background: var(--crimson); }
  .tab.spa { width: 62px; background: var(--plum); }
  .tab.gift { width: 60px; background: var(--magenta); }

  /* Intro */
  .intro { position: absolute; left: 86px; top: 750px; width: 1030px; font-size: 20px; line-height: 1.1; letter-spacing: 0.6px; color: var(--ink); }

  /* Dark feature band */
  .feature-band { position: absolute; left: 79px; top: 827px; width: 1042px; height: 227px; background: var(--night); }
  .feature-band .divider { position: absolute; left: 447px; top: 0; width: 1px; height: 227px; background: #2a2420; }
  .feature-band h2 { position: absolute; font-weight: 400; font-size: 19px; color: var(--pink-head); letter-spacing: 0.8px; }
  .testimonial h2 { left: 27px; top: 29px; }
  .client-photo { position: absolute; left: 28px; top: 66px; width: 116px; height: 113px;
    background: radial-gradient(ellipse at 50% 45%, #b08a6a, #5a3f2c 60%, #1c1410); }
  .quote { position: absolute; left: 159px; top: 98px; width: 205px; font-family: "Tinos", serif;
    font-size: 12px; line-height: 1.25; color: var(--link-purple); }
  .newcomer h2 { left: 507px; top: 29px; }
  .newcomer ul { position: absolute; left: 507px; top: 99px; list-style: none; font-family: "Tinos", serif;
    font-size: 12px; line-height: 19px; color: var(--link-purple); }
  .therapy-photo { position: absolute; left: 764px; top: 43px; width: 278px; height: 184px;
    background: linear-gradient(135deg, #2b1d16 0%, #c9a58a 45%, #efe7df 70%, #a8866e 100%); }

  /* Footer */
  .site-footer { position: absolute; left: 79px; top: 1056px; width: 1042px; height: 133px; background: var(--footer); }
  .footer-col { position: absolute; top: 36px; list-style: none; font-family: "Tinos", serif; font-size: 10px; font-weight: 700; line-height: 12.5px; color: var(--ink); }
  .footer-col:nth-child(1) { left: 58px; }
  .footer-col:nth-child(2) { left: 228px; }
  .footer-col:nth-child(3) { left: 426px; }
  .footer-col:nth-child(4) { left: 624px; }
  .footer-col:nth-child(5) { left: 832px; }
</style>
</head>
<body>
  <div class="page-frame"></div>

  <header class="site-header">
    <div class="brand">
      <div class="brand-name">calm harbour</div>
      <div class="brand-tagline">on location &amp; workplace</div>
    </div>

    <div class="social one" aria-label="Follow us: 2,078 followers">
      <span class="icon"></span><span class="count">2,078</span><span class="join">Join</span>
    </div>
    <div class="social two" aria-label="Like us: 1,455 fans">
      <span class="icon"></span><span class="count">1,455</span><span class="join">Join</span>
    </div>

    <div class="contact">
      <div class="phone">Phone: <strong>(08) 9415 2870</strong></div>
      <span class="message-link">Send us a message</span>
    </div>
    <div class="util-links"><span>OWN A FRANCHISE</span><span>FIND LOCATION</span></div>
  </header>

  <nav class="main-nav">
    <a>Welcome</a><a>Massage</a><a>Facials</a><a>Membership</a><a>Your First Visit</a><a>Get Started</a><a>Gift Cards</a><a>Locations</a>
  </nav>

  <section class="hero">
    <div class="hero-photo" role="img" aria-label="Photo of a relaxed woman resting with a flower in her hair, warm orange tones"></div>
    <div class="hero-panel">
      <h2>Choose Your Therapeutic Massage Type</h2>
      <p>FIND THE MASSAGE AND THERAPY THAT FITS YOUR NEEDS THEN ASK FOR THEM BY NAME.</p>
      <h3>Customize Your Massage Session</h3>
      <div class="where">WHERE DO YOU WANT IT</div>
      <div class="options"><span>+ ON LOCATION</span><span>+ WORKPLACE</span></div>
    </div>
    <div class="hero-tabs">
      <div class="tab massage"><span>MASSAGE</span></div>
      <div class="tab facial"><span>FACIAL</span></div>
      <div class="tab spa"><span>SPA</span></div>
      <div class="tab gift"><span>GIFT CARD</span></div>
    </div>
  </section>

  <p class="intro">Lorem ipsum dolor sit amet, consec tetuer adipiscing elit. Praesent vestibulum molestie lacus. Aenean nonummy hendrerit mauris.</p>

  <section class="feature-band">
    <div class="testimonial">
      <h2>Client’s Speak</h2>
      <div class="client-photo" role="img" aria-label="Portrait photo of a smiling client"></div>
      <p class="quote">Maecenas tristique orci ac sem. Duis ultricies pharetra magna. Donec accumsan malesuada orci. Donec sit amet eros. Lorem ipsum dolor sit amet, consectetuer adipiscing elit.</p>
    </div>
    <div class="divider"></div>
    <div class="newcomer">
      <h2>New to Calm Harbour?</h2>
      <ul>
        <li>New to Massage?</li>
        <li>Types of Massage</li>
        <li>Benefits of Massage Therapy</li>
        <li>Types of Facials</li>
      </ul>
      <div class="therapy-photo" role="img" aria-label="Photo of a therapist giving a client a head massage"></div>
    </div>
  </section>

  <footer class="site-footer">
    <ul class="footer-col"><li>About Us</li><li>Press Room</li><li>Own a Franchise</li></ul>
    <ul class="footer-col"><li>Corporate Wellness Program</li><li>Spa</li><li>Directory of Clinics</li></ul>
    <ul class="footer-col"><li>Corporate Wellness Program</li><li>Spa</li><li>Directory of Clinics</li></ul>
    <ul class="footer-col"><li>Corporate Wellness Program</li><li>Spa</li><li>Directory of Clinics</li></ul>
    <ul class="footer-col"><li>Corporate Wellness Program</li><li>Spa</li><li>Directory of Clinics</li></ul>
  </footer>
</body>
</html>
```